Velto Kin needs some awesome stationary

Do you have what it takes to get my brand? You either do or you don't, have a crack at a design and you my just win my business.

I don't want to waste your or my time, so put your creative genius on either a business card or envelope.

I however need a package of stationary that follows the same brand. I will message you to complete the remaining should I like your first submission.

Here is what I need, have a go!

Basically I need the following for my small business based in melbourne.
- Letterhead (printer ready and MS Word)
- Business Card
- Compliments Slip
- Envelope
- Proposal Cover Page (MS Word only)
- Presentation Folder
- Planning Poker Cards
- Student Name Tent
- Index Cards
- Dabble-Tab

I am establishing the brand and it must be modern, professional but also relaxed; that is not formal and not corporate. It represents a company are leaders, but small enough to care and operate like a bunch of friends. We are bringing people and conversations back to business, and turfing out all the bureaucracy and crazy and wasteful procedures. Its about "lets talk and figure it out together and find even better ways".

Target Market(s)

Mainly companies that build software products, but Agile practices are used in many other industries (even graphic design projects)

Industry/Entity Type

Information Technology

Font styles to use
Sans Serif

Colors
3176b5
aaaaaa

Requirements
Must have
• I like curves and circles and not boxes or rectangles.
• I want a colour rich design with my brand colours, but it must be balanced.
• I want more modern than traditional, but simple modern
Should not have
• Not corporate
• Please don't waste my time if your not going to think about it.
• Don't mess with my primary logo
• Don't change my colours
• Don't overlay logo on image

```html
<!DOCTYPE html>
<html lang="en">
<head>
<meta charset="utf-8">
<title>Velto Kin Stationery</title>
<link href="https://fonts.googleapis.com/css2?family=Open+Sans:wght@400;600&display=swap" rel="stylesheet">
<style>
  :root{
    --brand-blue:#0e519e;
    --bright-blue:#3176b5;
    --edge-blue:#1a8fd8;
    --brand-grey:#aaaaaa;
    --text-grey:#7a7a7a;
    --pattern-blue:#d6e6f6;
    --paper:#ffffff;
    --backdrop:#eef1f5;
  }
  *{margin:0;padding:0;box-sizing:border-box}
  html,body{width:1200px;height:1200px;overflow:hidden}
  body{background:var(--backdrop);font-family:"Open Sans",sans-serif;position:relative}

  .slip{
    position:absolute;left:150px;top:60px;width:900px;height:450px;
    background:var(--paper);border-bottom:10px solid var(--edge-blue);
    box-shadow:0 6px 18px rgba(0,0,0,.12);
  }
  .slip__tab-left{position:absolute;left:0;top:40px;width:6px;height:70px;background:var(--brand-blue)}
  .slip__tab-right{position:absolute;right:0;bottom:60px;width:6px;height:70px;background:var(--brand-grey)}

  .brand{position:absolute;display:flex;align-items:center;gap:12px;
    color:var(--brand-blue);font-weight:600;white-space:nowrap}
  .brand__dot{border-radius:50%;background:var(--brand-blue);flex:none}
  .slip .brand{left:50px;top:50px;font-size:40px}
  .slip .brand__dot{width:44px;height:44px}

  .contacts{position:absolute;left:50px;right:50px;bottom:26px;
    display:flex;justify-content:space-between;align-items:center;
    font-size:15px;color:var(--text-grey)}
  .contact{display:flex;align-items:center;gap:8px}
  .contact svg{width:18px;height:18px;fill:var(--brand-blue)}

  .envelope{position:absolute;left:150px;top:560px;width:900px;height:580px}
  .envelope svg.envelope__shape{position:absolute;inset:0;width:900px;height:580px}
  .envelope .brand{left:50%;top:390px;transform:translateX(-50%);font-size:34px}
  .envelope .brand__dot{width:38px;height:38px}
</style>
</head>
<body>

<section class="slip" aria-label="Compliments slip">
  <div class="slip__tab-left"></div>
  <div class="slip__tab-right"></div>
  <div class="brand"><span class="brand__dot"></span>Velto Kin</div>

  <ul class="contacts" style="list-style:none">
    <li class="contact">
      <svg viewBox="0 0 24 24"><path d="M12 2a7 7 0 0 0-7 7c0 5 7 13 7 13s7-8 7-13a7 7 0 0 0-7-7zm0 9.5A2.5 2.5 0 1 1 12 6.5a2.5 2.5 0 0 1 0 5z"/></svg>
      PO Box 4817, Brackenwood, VIC 3190, Australia
    </li>
    <li class="contact">
      <svg viewBox="0 0 24 24"><path d="M6.6 10.8a15 15 0 0 0 6.6 6.6l2.2-2.2a1 1 0 0 1 1-.25 11.4 11.4 0 0 0 3.6.57 1 1 0 0 1 1 1V20a1 1 0 0 1-1 1A17 17 0 0 1 3 4a1 1 0 0 1 1-1h3.5a1 1 0 0 1 1 1c0 1.25.2 2.45.57 3.57a1 1 0 0 1-.25 1z"/></svg>
      1300 482 615
    </li>
    <li class="contact">
      <svg viewBox="0 0 24 24"><path d="M2 5h20v14H2z M2 5l10 8 10-8" fill="var(--brand-blue)"/><path d="M3 6l9 7 9-7" fill="none" stroke="#fff" stroke-width="1.5"/></svg>
      hello@veltokin.com.au
    </li>
    <li class="contact">
      <svg viewBox="0 0 24 24"><circle cx="12" cy="12" r="10"/><path d="M2 12h20M12 2c3 3 3 17 0 20M12 2c-3 3-3 17 0 20" fill="none" stroke="#fff" stroke-width="1.3"/></svg>
      www.veltokin.com.au
    </li>
  </ul>
</section>

<section class="envelope" aria-label="DL envelope">
  <svg class="envelope__shape" viewBox="0 0 900 580">
    <polygon class="envelope__flap" points="60,0 840,0 900,120 0,120" fill="var(--brand-blue)"/>
    <rect class="envelope__inside" x="0" y="120" width="900" height="460" fill="var(--paper)"/>
    <polygon class="envelope__front" role="img" aria-label="Light blue repeating swirl pattern across the envelope front"
      points="0,120 30,120 450,210 870,120 900,120 900,580 0,580" fill="var(--pattern-blue)"/>
  </svg>
  <div class="brand"><span class="brand__dot"></span>Velto Kin</div>
</section>

</body>
</html>
```